Unternehmen für Wimpernverlängerung & -lifting benötigt Flyer-Design
Zielgruppe
Wimpernverlängerung, Wimpernlifting, Permanent Make-Up, Microblading, BB Glow, Hyaluron Pen
Aufgabenstellung
es soll eine preisliste werden, ich möchte die preise selbst einsetzen
produkte:
Wimpernverlängerung:
Natural Look
Auffüllen bis 1-2 Wochen
Auffüllen bis 3-4 Wochen
Ab der 5. Woche Neupreis
Volumen Look
Wimpernlifting inkl. färben
Microblading
Permanent Make-Up:
Powder Brows
Powder Brows Combo (Härchen&Shading)
Wimpernkranzverdichtung
Lidstrich dekorativ
Aquarelle Lips
Lippen Vollschattierung
BB Glow
Hyaluron Pen
Termine nach Vereinbarung

```html
<!DOCTYPE html>
<html lang="de">
<head>
<meta charset="utf-8">
<title>Lid Lumen – Preisliste</title>
<link rel="stylesheet" href="https://fonts.googleapis.com/css2?family=Dancing+Script:wght@600;700&family=Encode+Sans+Semi+Condensed:wght@400;500;600&display=swap">
<style>
  :root {
    --plum: #4b154d;
    --mauve: #974d82;
    --rose: #cb6f9e;
    --pink: #ea89b4;
    --blush: #f6d6e6;
    --white: #ffffff;
    --stage: #f1edf0;
    --text-font: "Encode Sans Semi Condensed", "Arial Narrow", sans-serif;
    --script-font: "Dancing Script", cursive;
  }
  * { margin: 0; padding: 0; box-sizing: border-box; }
  html, body { width: 1171px; height: 1200px; overflow: hidden; }
  body { background: var(--stage); position: relative; font-family: var(--text-font); }

  .flyer {
    position: absolute;
    top: 60px;
    width: 540px;
    height: 1080px;
    overflow: hidden;
    box-shadow: 0 6px 18px rgba(60, 20, 60, 0.25);
  }
  .flyer--front { left: 20px; }
  .flyer--back { left: 611px; }
  .flyer__bg { position: absolute; inset: 0; width: 100%; height: 100%; }

  /* Front: price list */
  .price-title {
    position: absolute; left: 50px; top: 42px;
    font-family: var(--script-font); font-weight: 700;
    font-size: 58px; color: var(--white); line-height: 1;
  }
  .appointment-note {
    position: absolute; left: 370px; top: 92px; width: 160px;
    font-family: var(--script-font); font-weight: 600;
    font-size: 21px; line-height: 24px; color: var(--white);
    transform: rotate(3deg);
  }
  .appointment-note span { display: block; }
  .appointment-note span + span { padding-left: 36px; }

  .price-group { position: absolute; left: 42px; width: 420px; color: var(--white); }
  .price-group__heading {
    font-weight: 600; font-size: 23px; letter-spacing: 0.2px;
    line-height: 26px; margin-bottom: 10px;
  }
  .price-list { list-style: none; }
  .price-list li {
    position: relative; font-size: 19px; line-height: 26px; height: 26px;
  }
  .price-list li.gap { margin-top: 16px; }
  .price-list .euro { position: absolute; left: 389px; top: 0; }

  .brand {
    position: absolute; left: 0; width: 100%; text-align: center;
    font-family: var(--text-font); font-weight: 500;
    color: var(--plum); letter-spacing: 1px; line-height: 1;
  }
  .flyer--front .brand { top: 960px; font-size: 52px; }

  /* Back: image and contact */
  .photo-area {
    position: absolute; left: 0; top: 0; width: 540px; height: 700px;
    background: linear-gradient(160deg, #8a7696 0%, #b8a6bc 40%, #cdb8c8 70%, #c4a9bf 100%);
  }
  .flyer--back .brand { top: 828px; font-size: 52px; }
  .contact {
    position: absolute; left: 0; top: 930px; width: 100%;
    text-align: center; color: var(--plum);
    font-size: 16px; line-height: 25px;
  }
</style>
</head>
<body>

<section class="flyer flyer--front" aria-label="Preisliste">
  <svg class="flyer__bg" viewBox="0 0 540 1080" preserveAspectRatio="none" aria-hidden="true">
    <defs>
      <linearGradient id="fade-front" x1="0" y1="0" x2="1" y2="0">
        <stop offset="0" stop-color="#f3bfd8"/>
        <stop offset="0.6" stop-color="#fbeef4"/>
        <stop offset="1" stop-color="#ffffff"/>
      </linearGradient>
    </defs>
    <rect width="540" height="1080" fill="var(--plum)"/>
    <path d="M0 0 H449 C 360 60, 200 132, 0 121 Z" fill="var(--pink)"/>
    <path d="M300 108 C 330 118, 360 128, 396 112 L 346 146 C 330 140, 312 124, 300 108 Z" fill="var(--white)"/>
    <polygon points="351,77 540,86 540,152 346,146" fill="var(--pink)"/>
    <path d="M0 852 C 150 730, 350 650, 540 641 V1080 H0 Z" fill="var(--mauve)"/>
    <path d="M0 921 C 170 800, 360 720, 540 710 V1080 H0 Z" fill="var(--rose)"/>
    <path d="M0 1000 C 170 870, 360 800, 540 790 V1080 H0 Z" fill="url(#fade-front)"/>
  </svg>

  <h1 class="price-title">Preise</h1>
  <p class="appointment-note"><span>Termine nach</span><span>Vereinbarung</span></p>

  <div class="price-group" style="top:136px">
    <h2 class="price-group__heading">WIMPERNVERLÄNGERUNG</h2>
    <ul class="price-list">
      <li>Natural Look<span class="euro">€</span></li>
      <li>Auffüllen bis 1-2 Wochen<span class="euro">€</span></li>
      <li>Auffüllen bis 3-4 Wochen<span class="euro">€</span></li>
      <li>Ab der 5. Woche Neupreis<span class="euro">€</span></li>
      <li class="gap">Volumen Look<span class="euro">€</span></li>
      <li>Auffüllen bis 1-2 Wochen<span class="euro">€</span></li>
      <li>Auffüllen bis 3-4 Wochen<span class="euro">€</span></li>
      <li>Ab der 5. Woche Neupreis<span class="euro">€</span></li>
      <li class="gap">Wimpernlifting ink. Färben<span class="euro">€</span></li>
      <li class="gap">Microblading<span class="euro">€</span></li>
    </ul>
  </div>

  <div class="price-group" style="top:509px">
    <h2 class="price-group__heading">PERMANENT MAKE-UP</h2>
    <ul class="price-list">
      <li>Powder Brows<span class="euro">€</span></li>
      <li>Powder Brows Combo (Härchen &amp; Shading)<span class="euro">€</span></li>
      <li>Wimpernkranzverdichtung<span class="euro">€</span></li>
      <li>Lidstrich dekorativ<span class="euro">€</span></li>
      <li>Aquarelle Lips<span class="euro">€</span></li>
      <li>Lippen Vollschattierung<span class="euro">€</span></li>
      <li class="gap">BB Glow<span class="euro">€</span></li>
      <li class="gap">Hyaloren Pen<span class="euro">€</span></li>
    </ul>
  </div>

  <p class="brand">LID LUMEN</p>
</section>

<section class="flyer flyer--back" aria-label="Rückseite mit Kontakt">
  <div class="photo-area" role="img" aria-label="Foto: geschlossenes Auge mit langen Wimpern und zartem Lidschatten"></div>
  <svg class="flyer__bg" viewBox="0 0 540 1080" preserveAspectRatio="none" aria-hidden="true">
    <defs>
      <linearGradient id="fade-back" x1="0" y1="0" x2="1" y2="0">
        <stop offset="0" stop-color="#f3bfd8"/>
        <stop offset="0.6" stop-color="#fbeef4"/>
        <stop offset="1" stop-color="#ffffff"/>
      </linearGradient>
    </defs>
    <path d="M0 720 C 150 620, 360 560, 540 551 V1080 H0 Z" fill="#e39bc0" opacity="0.9"/>
    <path d="M0 790 C 170 690, 360 630, 540 620 V1080 H0 Z" fill="var(--rose)" opacity="0.85"/>
    <path d="M0 860 C 170 760, 360 710, 540 700 V1080 H0 Z" fill="url(#fade-back)"/>
  </svg>

  <p class="brand">LID LUMEN</p>
  <p class="contact">
    Mirabel Tosch - 12345 Musterstadt/Nord - Tel.: 0176 55501234<br>
    www.lid-lumen.de<br>
    facebookseite: lid_lumen25<br>
    instagram: lid_lumen_de
  </p>
</section>

</body>
</html>
```